Halvorn spray foam and Environmental

I have business cards but need new ones. The ones I have are very bland. Here is. Y company website http://www.halvornsprayfoam.ca

Also I can send you copies of the current cards
I would also need my current logo on the new design as well.. Also spray foam and Environmental

Industry/Entity Type

Business

Logo Text

Halvorn.

```html
<!DOCTYPE html>
<html lang="en">
<head>
<meta charset="utf-8">
<title>Halvorn business cards</title>
<link rel="stylesheet" href="https://fonts.googleapis.com/css2?family=Roboto:wght@400;500;700&display=swap">
<style>
  :root {
    --bg: #181a1a;
    --card-base: #f1f1f1;
    --band-grey: #cbc8c8;
    --band-grey-foam: #d4d2d2;
    --band-white: #f7f7f7;
    --green: #069444;
    --purple: #74468e;
    --ink: #3d3d3d;
    --ink-soft: #4a4a4a;
    --rule: #4b4b4b;
    --mark-grey: #8a8585;
  }
  * { box-sizing: border-box; margin: 0; padding: 0; }
  html, body {
    width: 1200px; height: 1000px; overflow: hidden;
    background: var(--bg);
    font-family: "Roboto", Arial, sans-serif;
  }
  .stage { position: relative; width: 1200px; height: 1000px; }
  .card {
    position: absolute; left: 290px;
    width: 620px; height: 354px;
    border-radius: 18px; overflow: hidden;
    background: var(--card-base);
  }
  .card--environmental { top: 110px; }
  .card--sprayfoam { top: 536px; }
  .card-shapes { position: absolute; inset: 0; width: 100%; height: 100%; }
  .brand {
    position: absolute; left: 60px; top: 62px; width: 170px;
    text-align: center; color: var(--ink);
  }
  .brand-square {
    width: 86px; height: 86px; margin: 0 auto 10px;
    background: var(--mark-grey);
  }
  .brand-name {
    font-weight: 700; font-size: 34px; line-height: 1; letter-spacing: 0.5px;
    text-transform: uppercase;
  }
  .brand-sub {
    font-weight: 700; font-size: 16px; line-height: 1.15;
    text-transform: uppercase; letter-spacing: 0.6px;
  }
  .card--sprayfoam .brand-sub { font-size: 22px; }
  .divider {
    position: absolute; left: 250px; top: 70px;
    width: 2px; height: 210px; background: var(--rule);
  }
  .contact {
    position: absolute; left: 280px; top: 80px;
    color: var(--ink-soft); font-size: 17px; line-height: 1.3;
    list-style: none;
  }
  .card--sprayfoam .contact { font-size: 19px; }
  .services {
    position: absolute; left: 280px; top: 230px;
    color: var(--ink); font-weight: 500; font-size: 14px; line-height: 1.3;
    text-transform: uppercase; letter-spacing: 0.3px;
  }
  .card--sprayfoam .services { font-size: 15px; font-weight: 700; }
</style>
</head>
<body>
<main class="stage">

  <article class="card card--environmental">
    <svg class="card-shapes" viewBox="0 0 620 354" preserveAspectRatio="none" aria-hidden="true">
      <defs>
        <linearGradient id="lavEnv" x1="0" y1="0" x2="1" y2="0.4">
          <stop offset="0" stop-color="#d7cce1"/>
          <stop offset="1" stop-color="#f4f1f5"/>
        </linearGradient>
      </defs>
      <path d="M230 0 H620 V170 C520 160 360 140 270 80 C245 55 235 25 230 0 Z" fill="url(#lavEnv)"/>
      <path d="M0 170 C150 195 380 200 620 205 V354 H0 Z" fill="var(--band-white)"/>
      <path d="M0 205 C170 228 390 222 620 220 V354 H0 Z" fill="var(--band-grey)"/>
      <path d="M0 255 C120 262 200 300 250 354 H0 Z" fill="var(--band-white)"/>
      <path d="M0 275 C100 280 170 310 205 354 H0 Z" fill="var(--green)"/>
      <path d="M620 150 L505 200 L620 204 Z" fill="var(--green)"/>
    </svg>
    <div class="brand">
      <div class="brand-square"></div>
      <div class="brand-name">Halvorn</div>
      <div class="brand-sub">Environmental</div>
    </div>
    <div class="divider"></div>
    <ul class="contact">
      <li>604-555-0142</li>
      <li>enviro1@halvornmail.ca</li>
      <li>www.halvornenvironmental.ca</li>
    </ul>
    <p class="services">
      Air Monitoring | Asbestos Testing<br>
      Asbestos Removal | Building Demolition<br>
      Lead Testing | Mould Removal
    </p>
  </article>

  <article class="card card--sprayfoam">
    <svg class="card-shapes" viewBox="0 0 620 354" preserveAspectRatio="none" aria-hidden="true">
      <defs>
        <linearGradient id="lavFoam" x1="0" y1="0" x2="1" y2="0.4">
          <stop offset="0" stop-color="#d9cfe3"/>
          <stop offset="1" stop-color="#f4f1f5"/>
        </linearGradient>
      </defs>
      <path d="M230 0 H620 V170 C520 160 360 140 270 80 C245 55 235 25 230 0 Z" fill="url(#lavFoam)"/>
      <path d="M0 170 C150 195 380 200 620 205 V354 H0 Z" fill="var(--band-white)"/>
      <path d="M0 205 C170 228 390 222 620 220 V354 H0 Z" fill="var(--band-grey-foam)"/>
      <path d="M0 255 C120 262 200 300 250 354 H0 Z" fill="var(--band-white)"/>
      <path d="M0 275 C100 280 170 310 205 354 H0 Z" fill="var(--purple)"/>
      <path d="M620 150 L505 200 L620 204 Z" fill="var(--purple)"/>
    </svg>
    <div class="brand">
      <div class="brand-square"></div>
      <div class="brand-name">Halvorn</div>
      <div class="brand-sub">Spray Foam</div>
    </div>
    <div class="divider"></div>
    <ul class="contact">
      <li>(604) 555-0187</li>
      <li>halvornfoam@halvornmail.ca</li>
      <li>www.halvornsprayfoam.ca</li>
    </ul>
    <p class="services">
      Roofing Foam | Slab Jacking<br>
      2 Pound/Halfpound | Sound Proofing<br>
      Batt Insulation | Attic Blow In
    </p>
  </article>

</main>
</body>
</html>
```